Poster Design Project- kids dancing/sport

I need a poster design for a childrens dance and sport program!!
I have attached a brochure and logo designs. From the brochure please include information from sections titled "twirl'n'hop" and "themes". Also please put on the phone number and email address (found on the brochure). Emphasis on FUN!! Make poster colourful, very kid friendly and eye catching.
Some other things i would like on the poster are:
"Does your child love to dance, sing and play sport?? Why not enrol them in our fun-filled program?"
"From only $10.00 per class"
"Sign up for your FREE trial class today"
"A fun introduction to the joy of Dance, Sport and Music for 2-6yr olds. Held in your childcare centre!!"
Hi!!
I would like to stress its TRIAL class not TRAIL class. Please feel free to play around with the information, it doesnt need to be in one blurb. Also i have updated the brief. I would like "Does you child love to dance, sing or play sport? Why not enrol in our fun filled program?" or something to that effect!!
Thanks!!!!
2-6yr olds and their parents
Childcare

```html
<!DOCTYPE html>
<html lang="en">
<head>
<meta charset="utf-8">
<title>Twirl 'n' Hop – Dance, Sport and Music for Kids</title>
<link href="https://fonts.googleapis.com/css2?family=Comic+Neue:wght@400;700&display=swap" rel="stylesheet">
<style>
  :root {
    --lime: #c9ec2a;
    --lime-pale: #eef9a8;
    --paper: #ffffff;
    --headline-red: #ee1c24;
    --sky-blue: #3ab4e4;
    --orange: #f7941d;
    --magenta: #e430c8;
    --leaf-green: #6cc81c;
    --panel-grey: #f1f1f1;
    --brand-ink: #e0218a;
  }
  * { box-sizing: border-box; margin: 0; padding: 0; }
  html, body { width: 852px; height: 1200px; overflow: hidden; background: var(--paper); }
  body { font-family: "Comic Neue", "Comic Sans MS", cursive; }

  .poster { position: relative; width: 852px; height: 1200px; overflow: hidden; background: var(--paper); }

  .starburst-backdrop {
    position: absolute; left: 0; top: 0; width: 852px; height: 1000px;
    background:
      radial-gradient(ellipse 420px 330px at 560px 260px, var(--paper) 0%, var(--paper) 55%, rgba(255,255,255,0) 100%),
      radial-gradient(ellipse 700px 520px at 430px 640px, var(--lime-pale) 0%, var(--lime) 100%);
  }

  .dancers-scene {
    position: absolute; left: 0; top: 560px; width: 852px; height: 330px;
    background:
      linear-gradient(90deg, rgba(140,220,40,.55) 0%, rgba(238,28,36,.35) 22%, rgba(247,148,29,.35) 38%, rgba(58,180,228,.4) 62%, rgba(228,48,200,.4) 82%, rgba(150,70,200,.3) 100%),
      linear-gradient(180deg, rgba(255,255,255,0) 0%, rgba(255,255,255,.5) 100%);
    border-radius: 40px 40px 0 0;
  }

  .headline-block {
    position: absolute; left: 130px; top: 10px; width: 740px;
    transform: rotate(8deg); transform-origin: 0 0;
    text-align: center; font-weight: 700;
  }
  .headline { color: var(--headline-red); font-size: 40px; line-height: 44px; }
  .question { color: var(--sky-blue); font-size: 25px; line-height: 30px; margin-top: 6px; }
  .trial-offer { color: var(--orange); font-size: 27px; line-height: 30px; margin-top: 8px; }
  .themes-list {
    color: var(--headline-red); font-size: 15.5px; line-height: 18px; font-weight: 400;
    margin-top: 10px; padding: 0 20px;
  }

  .price-badge {
    position: absolute; left: 35px; top: 410px; width: 158px; height: 158px;
    border-radius: 50%; background: var(--sky-blue); color: var(--paper);
    display: flex; flex-direction: column; align-items: center; justify-content: center;
    font-weight: 700; text-align: center;
  }
  .price-badge .lead { font-size: 22px; line-height: 24px; }
  .price-badge .amount { font-size: 40px; line-height: 44px; }
  .price-badge .unit { font-size: 22px; line-height: 24px; }

  .contact-panel {
    position: absolute; left: 48px; top: 890px; width: 766px; height: 110px;
    background: var(--panel-grey); color: var(--magenta);
    font-weight: 700; font-size: 38px; line-height: 46px; padding: 10px 0 0 40px;
  }
  .contact-panel .phone { padding-left: 112px; }

  .brand-mark {
    position: absolute; left: 18px; top: 1005px; width: 176px; height: 72px;
    display: flex; align-items: center; gap: 8px;
    color: var(--brand-ink); font-weight: 700; font-size: 22px;
  }
  .brand-mark .dot { width: 18px; height: 18px; border-radius: 50%; background: var(--brand-ink); flex: none; }

  .about-blurb {
    position: absolute; left: 204px; top: 1020px; width: 636px;
    color: var(--leaf-green); font-size: 10.4px; line-height: 12.6px;
  }
</style>
</head>
<body>
<main class="poster">
  <div class="starburst-backdrop" role="img" aria-label="Lime green starburst background with white stars and halftone dots"></div>
  <div class="dancers-scene" role="img" aria-label="Colourful silhouettes of children dancing, singing and playing guitar over piano keys and music notes"></div>

  <section class="headline-block">
    <h1 class="headline">Does your child love to<br>dance, sing and play sport??</h1>
    <p class="question">Why not enrol them in our fun-filled program?</p>
    <p class="trial-offer">Sign up for your FREE trial class today<br>A fun introduction to the joy of Dance, Sport and<br>Music for 2-6yr olds. Held in your childcare centre!!</p>
    <p class="themes-list">Jumping Jellybeans, Under the Sea, Superheros, Jungle Jam, Storybook, Balancing Bugs Gymnastics and Rhythmic Gymnastics, Disco Divas and Singing Superstars Hawaiian Holiday, Circus, Space, Bowling and Ball Skills, Colours and Shapes Monsters, Magical Fairytales, Sport and Cheerleading, Mexican Fiesta, Animals Aboriginal Adventure, Its Party Time</p>
  </section>

  <div class="price-badge">
    <span class="lead">From only</span>
    <span class="amount">$10.00</span>
    <span class="unit">per class</span>
  </div>

  <section class="contact-panel">
    <p class="phone">Phone: 0400 512 786</p>
    <p class="email">Email: twirlnhop@kidsmail.com</p>
  </section>

  <div class="brand-mark"><span class="dot"></span><span>Twirl 'n' Hop</span></div>

  <p class="about-blurb">Twirl 'n' Hop offers little boys and girls a range of FUN classes, held in your childcare centre, that will introduce them to the wonderful world of music, movement and P.E. Every class is a magical place to be with funky music, props, puppets, costumes and exciting equipment! Children will develop a range of skills including balance, co-ordination, confidence, motor skills, creativity, rhythm and much more!! Each fortnight there is a different theme where children can express themselves and explore many dance genres as well as yoga, gymnastics, sport, musical instruments and ball skills. Detailed information on each class will be emailed to you every fortnight so you'll always be kept up-to-date with what your child is learning!! Twirl 'n' Hop also offers birthday parties!!! You can select any of the themes listed, or we can custom make a party to the interest of your child. Your host will come dressed as a character of your choice and keep the children entertained for 1-2hrs. Email us for more information!!</p>
</main>
</body>
</html>
```